Calder Pizza - Takeout Menu Design

We are looking for a takeout menu design.
We are looking for a( 5" x 8.5" DOUBLE SIDED) flyer with our available pizza flavors
Must be easy to ready and not "busy"

Must include our logo (attached)
website: www.calderpizza.ca
address:
Fenwick Ridge Plaza
417, 318 9 Avenue SW
and the following details:
Visit our website for our complete appetizer, pasta, salad and catering menu.

Winner of this contest will also be offered to create a few print designs via printhive.

Please do not hesitate to ask any questions.

Target Market(s)

Business / Office clientele

Industry/Entity Type

Pizza place / specializing in corporate orders

Requirements
Must have
• Easy to read
Should not have
• Can not be busy or cluttered

```html
<!DOCTYPE html>
<html lang="en">
<head>
<meta charset="utf-8">
<title>Calder Pizza – Take-Out Menu</title>
<link rel="stylesheet" href="https://fonts.googleapis.com/css2?family=Fira+Sans+Extra+Condensed:wght@300;400;700&family=Open+Sans:wght@400&display=swap">
<style>
  :root {
    --red: #c0250f;
    --ink: #222222;
    --body: #4a4a4a;
    --rule: #9a9a9a;
    --frame: #1a1a1a;
    --paper: #ffffff;
  }
  * { box-sizing: border-box; margin: 0; padding: 0; }
  html, body { width: 1200px; height: 927px; overflow: hidden; background: var(--paper); }
  body { position: relative; font-family: "Fira Sans Extra Condensed", sans-serif; color: var(--body); }

  .page { position: absolute; top: 0; height: 927px; border: 1px solid var(--frame); border-top: none; overflow: hidden; background: var(--paper); }
  .page--specialty { left: 55px; width: 545px; border-right-width: 2px; }
  .page--classic { left: 600px; width: 546px; border-left-width: 1px; }

  .hero-band { position: absolute; left: 0; top: 0; width: 100%; height: 96px;
    background: linear-gradient(90deg, #5b3a22 0%, #b8452a 30%, #d9a66a 55%, #9a2f1e 80%, #6b4a2f 100%);
    box-shadow: 0 8px 14px rgba(0,0,0,0.25); }

  .menu-col { position: absolute; top: 144px; width: 243px; }
  .menu-col--a { left: 20px; }
  .menu-col--b { left: 282px; }

  .col-head { height: 30px; background: var(--red); color: #fff; font-weight: 700; font-size: 12.5px;
    display: grid; grid-template-columns: 163px 42px 1fr; align-items: center; padding-left: 14px;
    clip-path: polygon(0 0, 235px 0, 243px 8px, 243px 100%, 0 100%); letter-spacing: 0.2px; }
  .col-head span:first-child { padding-left: 0; }
  .col-head .sz { padding-left: 0; }
  .menu-list { margin-top: 1.5px; width: 238px; }

  .item, .desc, .gap { height: 18.18px; line-height: 18.18px; }
  .item { display: grid; grid-template-columns: 163px 42px 33px; color: var(--red); font-weight: 700; font-size: 13px;
    border-bottom: 1px dotted var(--rule); }
  .item .p { font-size: 12.5px; }
  .item--pickle { grid-template-columns: 82px 39px 43px 41px 33px; }
  .desc { font-weight: 300; font-size: 12px; color: var(--body); white-space: nowrap; }

  .col-divider { position: absolute; left: 272px; top: 144px; height: 664px; border-left: 1px dotted var(--rule); }

  .brand { position: absolute; left: 0; width: 100%; text-align: center; font-weight: 300;
    font-size: 34px; letter-spacing: 1px; color: var(--ink); }
  .brand .dot { display: inline-block; width: 18px; height: 18px; border-radius: 50%; background: var(--red); vertical-align: 4px; margin-right: 8px; }
  .page--specialty .brand { top: 840px; }
  .tagline { position: absolute; left: 0; width: 100%; text-align: center; font-family: "Open Sans", sans-serif; font-size: 10.5px; color: var(--ink); }
  .page--specialty .tagline { top: 882px; }

  .hero-pizza { position: absolute; left: 0; top: 0; width: 546px; height: 410px; }

  .classic { position: absolute; left: 90px; top: 468px; }
  .classic-row { display: grid; grid-template-columns: 204px 97px 80px; height: 27.3px; line-height: 27.3px; font-size: 21px; }
  .classic-row .name { font-weight: 300; color: var(--ink); }
  .classic-row .p { font-weight: 700; color: var(--red); }
  .classic-head { height: 30px; line-height: 30px; font-weight: 700; font-size: 22px; color: #000; }
  .classic-head .name, .classic-head .p { font-weight: 700; color: #000; }

  .page--classic .brand { top: 772px; }
  .address { position: absolute; top: 812px; width: 100%; text-align: center; font-size: 16px; color: #555; }
  .website { position: absolute; top: 834px; width: 100%; text-align: center; font-size: 15px; color: var(--red); }
  .page--classic .tagline { top: 868px; line-height: 14.5px; }
</style>
</head>
<body>

<section class="page page--specialty">
  <div class="hero-band" role="img" aria-label="Close-up photo of a loaded pizza with black olives, red onion and melted cheese"></div>

  <div class="col-divider"></div>

  <div class="menu-col menu-col--a">
    <div class="col-head"><span>SPECIALTY TAKE-OUT PIZZA</span><span class="sz">8″</span><span class="sz">13″</span></div>
    <div class="menu-list">
      <div class="item"><span>All Meat</span><span class="p">$14.99</span><span class="p">$35.95</span></div>
      <div class="desc">Pepperoni, Beef &amp; Smoked Ham &amp; Bacon</div>
      <div class="item"><span>Double Pepperoni</span><span class="p">$13.49</span><span class="p">$32.95</span></div>
      <div class="desc">Loads of Pepperoni</div>
      <div class="item"><span>Hot Honey Pepperoni</span><span class="p">$14.49</span><span class="p">$34.95</span></div>
      <div class="desc">Double Pepperoni and drizzled</div>
      <div class="desc">with Hot Honey</div>
      <div class="item"><span>Hawaiian Heat</span><span class="p">$13.49</span><span class="p">$32.95</span></div>
      <div class="desc">Smoked Ham, Pineapple and</div>
      <div class="desc">Banana Peppers.</div>
      <div class="item"><span>Four Cheese</span><span class="p">$13.49</span><span class="p">$32.95</span></div>
      <div class="desc">Mozzarella, Feta, Romano and Cheddar Cheese.</div>
      <div class="item"><span>Montreal</span><span class="p">$13.49</span><span class="p">$32.95</span></div>
      <div class="desc">Pepperoni &amp; Double Smoked Bacon.</div>
      <div class="item"><span>Montreal Heat</span><span class="p">$13.99</span><span class="p">$33.95</span></div>
      <div class="desc">Pepperoni, Double Smoked Bacon</div>
      <div class="desc">&amp; Banana Peppers.</div>
      <div class="item"><span>Supreme</span><span class="p">$13.49</span><span class="p">$32.95</span></div>
      <div class="desc">Pepperoni, Mushrooms &amp; Green Peppers.</div>
      <div class="item"><span>Canadian</span><span class="p">$13.49</span><span class="p">$32.95</span></div>
      <div class="desc">Pepperoni, Mushrooms &amp; Ham.</div>
      <div class="item"><span>BBQ Chicken</span><span class="p">$13.99</span><span class="p">$33.95</span></div>
      <div class="desc">Chicken Breast, Hickory BBQ Sauce.</div>
      <div class="item"><span>BBQ Chicken Plus</span><span class="p">$14.79</span><span class="p">$34.95</span></div>
      <div class="desc">Chicken Breast, Hickory BBQ Sauce,</div>
      <div class="desc">Red Onions &amp; Cilantro.</div>
      <div class="item"><span>Spicy BBQ Chicken</span><span class="p">$14.49</span><span class="p">$35.95</span></div>
      <div class="desc">Chicken Breast, Hickory BBQ Sauce,</div>
      <div class="desc">Red Onions &amp; Banana Peppers</div>
      <div class="item"><span>Sweet Chili Chicken</span><span class="p">$14.49</span><span class="p">$35.95</span></div>
      <div class="desc">Chicken Breast, Pineapple,</div>
      <div class="desc">Red Onions &amp; Sweet Chili Sauce.</div>
      <div class="item"><span>Chicken Club</span><span class="p">$14.79</span><span class="p">$35.95</span></div>
      <div class="desc">Chicken Breast, Double Smoked</div>
      <div class="desc">Bacon, Red Onions and Tomatoes.</div>
    </div>
  </div>

  <div class="menu-col menu-col--b">
    <div class="col-head"><span>SPECIALTY TAKE-OUT PIZZA</span><span class="sz">8″</span><span class="sz">13″</span></div>
    <div class="menu-list">
      <div class="item"><span>Athenean</span><span class="p">$14.49</span><span class="p">$34.95</span></div>
      <div class="desc">Chicken Breast, Spinach, Feta Cheese</div>
      <div class="desc">and Tomato.</div>
      <div class="item"><span>Greek Supreme</span><span class="p">$14.99</span><span class="p">$35.95</span></div>
      <div class="desc">Chicken Breast, Feta Cheese, Tomato,</div>
      <div class="desc">Green Pepper, Red Onions &amp; Black Olives.</div>
      <div class="item"><span>Mediterranean Chicken</span><span class="p">$14.79</span><span class="p">$35.95</span></div>
      <div class="desc">Seasoned Chicken Breast, Tomatoes,</div>
      <div class="desc">Red Onions and Feta Cheese.</div>
      <div class="item"><span>Original Spinach</span><span class="p">$13.49</span><span class="p">$32.95</span></div>
      <div class="desc">Spinach &amp; Feta Cheese.</div>
      <div class="item"><span>Zeus</span><span class="p">$13.95</span><span class="p">$33.95</span></div>
      <div class="desc">Spinach, Feta Cheese and Tomatoes.</div>
      <div class="item"><span>Greek</span><span class="p">$13.99</span><span class="p">$33.95</span></div>
      <div class="desc">Feta Cheese, Tomato, Green Peppers,</div>
      <div class="desc">Red Onions and Black Olives.</div>
      <div class="item"><span>Vegetarian</span><span class="p">$13.49</span><span class="p">$32.95</span></div>
      <div class="desc">Mushrooms, Tomatoes, Green</div>
      <div class="desc">Peppers and Black Olives.</div>
      <div class="item"><span>Veggie Delight</span><span class="p">$13.95</span><span class="p">$33.95</span></div>
      <div class="desc">Mushrooms, Tomatoes, Green</div>
      <div class="desc">Peppers, Black Olives &amp; Onions.</div>
      <div class="item"><span>Deluxe</span><span class="p">$14.49</span><span class="p">$34.95</span></div>
      <div class="desc">Pepperoni, Mushrooms, Ham,</div>
      <div class="desc">Tomatoes, Green Peppers &amp; Red Onions.</div>
      <div class="item"><span>Calder Special</span><span class="p">$14.49</span><span class="p">$34.95</span></div>
      <div class="desc">Pepperoni, Mushrooms, Ham,</div>
      <div class="desc">Green Peppers and Black Olives.</div>
      <div class="item item--pickle"><span>Dill Pickle</span><span class="p">$13.49</span><span class="p">$32.95</span><span class="p">$14.49</span><span class="p">$35.95</span></div>
      <div class="desc">Crispy Dill Pickles, Fresh Dill with our cream based garlic</div>
      <div class="desc">sauce. Served with our without bacon.</div>
      <div class="gap"></div>
      <div class="item"><span>BBQ Pulled Pork</span><span class="p">$14.49</span><span class="p">$35.95</span></div>
      <div class="desc">Pulled Pork, Red Onions,</div>
      <div class="desc">Red Peppers and Cilantro.</div>
    </div>
  </div>

  <div class="brand"><span class="dot"></span>CALDER PIZZA</div>
  <p class="tagline">All of our pizzas are prepared fresh everyday using only the finest mozzarella blend and ingredients.</p>
</section>

<section class="page page--classic">
  <svg class="hero-pizza" viewBox="0 0 546 410" aria-hidden="false">
    <defs>
      <linearGradient id="pizzaTone" x1="0" y1="0" x2="1" y2="1">
        <stop offset="0" stop-color="#c9542a"/>
        <stop offset="0.45" stop-color="#e8a35a"/>
        <stop offset="0.8" stop-color="#d9793a"/>
        <stop offset="1" stop-color="#b8421e"/>
      </linearGradient>
      <filter id="drop" x="-10%" y="-10%" width="120%" height="130%">
        <feDropShadow dx="0" dy="8" stdDeviation="7" flood-color="#000" flood-opacity="0.25"/>
      </filter>
    </defs>
    <path d="M0 0 H546 V235 C505 300 440 356 355 392 H70 C35 392 5 370 0 340 Z" fill="#c0250f" filter="url(#drop)"/>
    <path role="img" aria-label="Photo of a pizza topped with olives, peppers, onion, ham and basil" d="M0 0 H546 V228 C505 290 440 344 355 386 H70 C35 386 5 364 0 334 Z" fill="url(#pizzaTone)"/>
  </svg>

  <div class="classic">
    <div class="classic-row classic-head"><span class="name">Classic Take-Out Pizza</span><span class="p">8″</span><span class="p">13″</span></div>
    <div class="classic-row"><span class="name">Pepperoni &amp; Mushroom</span><span class="p">$12.99</span><span class="p">$30.95</span></div>
    <div class="classic-row"><span class="name">Pepperoni</span><span class="p">$11.99</span><span class="p">$29.95</span></div>
    <div class="classic-row"><span class="name">Hawaiian</span><span class="p">$12.99</span><span class="p">$30.95</span></div>
    <div class="classic-row"><span class="name">Beef &amp; Mushroom</span><span class="p">$13.49</span><span class="p">$32.95</span></div>
    <div class="classic-row"><span class="name">Pepperoni &amp; Ham</span><span class="p">$12.99</span><span class="p">$30.95</span></div>
    <div class="classic-row"><span class="name">Ham &amp; Mushroom</span><span class="p">$12.99</span><span class="p">$30.95</span></div>
    <div class="classic-row"><span class="name">Beef &amp; Onion</span><span class="p">$13.49</span><span class="p">$32.95</span></div>
    <div class="classic-row"><span class="name">Cheese</span><span class="p">$11.99</span><span class="p">$29.95</span></div>
  </div>

  <div class="brand"><span class="dot"></span>CALDER PIZZA</div>
  <p class="address">Fenwick Ridge Plaza 417, 318 9 Avenue SW</p>
  <p class="website">WWW.CALDERPIZZA.CA</p>
  <p class="tagline">Visit our website for our complete appetizer, pasta, salad and catering menu.<br>All of our pizzas are prepared fresh everyday using only the finest mozzarella blend and ingredients.</p>
</section>

</body>
</html>
```